eBook-Cover für mein Buch Wellen im Morgenlicht
Zielgruppe
Das Wichtigste zuerst! :-) Der Titel des Buches ist 'Wellen im Morgenlicht'. Der Autor ist Marlene Otterbach.
Aufgabenstellung
Da es sich um den zweiten Band handelt, möchte ich gern ein Cover, aus dem sich schließen lässt, dass beide Bücher zusammen gehören. Deshalb habe ich das erste Cover als Bild hinzugefügt.
Es kann gern wieder in schwarz-weiß sein, muss aber nicht.
Der Inhalt der Geschichte:
Es geht um Ilka, Jonas und Bernhard. Jonas macht Ilka einen Heiratsantrag, den Ilka annimmt. Einige Zeit später passiert ein Unfall. Bernhards Frau ist auf dem Weg zu einem Konzert. Sie läuft an einer Baustelle vorbei, auf welcher ein Kran steht und der Arm über ihr schwebt, sozusagen. Da der Kran überladen ist, fällt die Ladung nach unten und begräbt sie unter sich. Die Frau von Bernhard verunglückt tödlich, woraufhin er in ein tiefes Loch fällt. Er greift zu Alkohol und Tabletten, um seine Gefühle zu betäuben. Ilka will ihm helfen, von seiner Sucht loszukommen. Bernhard hat eine neue Patientin, mit welcher er dann auch eine Nacht verbringt. Danach beendet er jedoch die Sache gleich wieder. Trotzdem geht ihm die Frau nicht mehr aus dem Kopf. Schlussendlich macht er mit Ilka einen Entzug und Ilka und Jonas heiraten.
Auch bei diesem Cover wäre es gut, wenn man die Verbindung zur Musik wieder erkennt, da es im zweiten Buch auch wieder viel Musik gibt. Natürlich ist es gut, wenn man eine kleine Andeutung auf den Inhalt erhält. Allerdings sollte es nicht so offensichtlich sein. Das heißt, ich möchte nicht unbedingt eine Flasche Bier und eine Tablettenschachtel auf dem Cover haben. ;-)
Die Schriftart kann gern wieder in die Richtung vom ersten Cover gehen.
Ich benötige das Cover mit einer Mindestbreite von 1600 Pixeln. Ansonsten lasse ich mich überraschen!

```html
<!DOCTYPE html>
<html lang="de">
<head>
<meta charset="utf-8">
<title>Wellen im Morgenlicht – Marlene Otterbach</title>
<link rel="stylesheet" href="https://fonts.googleapis.com/css2?family=Questrial&family=Sacramento&display=swap">
<style>
  :root {
    --cover-black: #161616;
    --ink-white: #ffffff;
    --bloom-white: rgba(225, 225, 225, 0.75);
    --bloom-grey: rgba(130, 130, 130, 0.6);
    --bloom-violet: rgba(170, 120, 180, 0.75);
    --fade: rgba(22, 22, 22, 0);
  }
  html, body {
    margin: 0;
    padding: 0;
    overflow: hidden;
    background: var(--cover-black);
  }
  .cover {
    position: relative;
    width: 800px;
    height: 1200px;
    overflow: hidden;
    background: var(--cover-black);
  }
  .flower-photo {
    position: absolute;
    inset: 0;
    z-index: 0;
    background:
      radial-gradient(ellipse 40px 38px at 175px 38px, var(--bloom-white), var(--fade)),
      radial-gradient(ellipse 130px 90px at 270px 200px, var(--bloom-violet), var(--fade)),
      radial-gradient(ellipse 85px 60px at 510px 50px, var(--bloom-white), var(--fade)),
      radial-gradient(ellipse 78px 62px at 618px 250px, var(--bloom-white), var(--fade)),
      radial-gradient(ellipse 95px 80px at 90px 630px, var(--bloom-white), var(--fade)),
      radial-gradient(ellipse 75px 70px at 706px 690px, var(--bloom-white), var(--fade)),
      radial-gradient(ellipse 130px 95px at 370px 770px, var(--bloom-white), var(--fade)),
      radial-gradient(ellipse 115px 90px at 560px 830px, var(--bloom-grey), var(--fade)),
      radial-gradient(ellipse 130px 85px at 510px 965px, var(--bloom-violet), var(--fade)),
      radial-gradient(ellipse 120px 90px at 230px 1150px, var(--bloom-white), var(--fade)),
      var(--cover-black);
  }
  .author {
    position: absolute;
    top: 323px;
    left: 0;
    width: 760px;
    margin: 0;
    text-align: center;
    font-family: "Questrial", "Century Gothic", sans-serif;
    font-weight: 400;
    font-size: 38px;
    color: var(--ink-white);
    z-index: 1;
  }
  .title {
    position: absolute;
    top: 432px;
    left: 0;
    width: 800px;
    margin: 0;
    text-align: center;
    font-family: "Sacramento", cursive;
    font-weight: 400;
    font-size: 125px;
    line-height: 123px;
    color: var(--ink-white);
    z-index: 1;
  }
  .title-line { display: block; }
  .title-line--second { padding-left: 16px; }
</style>
</head>
<body>
<main class="cover">
  <div class="flower-photo" role="img" aria-label="Fotografie: weiße, graue und violette Nelken und Rosen vor schwarzem Hintergrund, oben hängend, unten aufrecht stehend"></div>
  <p class="author">Marlene Otterbach</p>
  <h1 class="title">
    <span class="title-line">Wellen im</span>
    <span class="title-line title-line--second">Morgenlicht</span>
  </h1>
</main>
</body>
</html>
```